LETTERHEAD & ENVELOPE: eye-catching stationary design for our custom office furniture business

Our company recently rebranded and we are in need of new stationary. Specifically, we need branded letterhead for standard paper size (8.5” x 11”), and matching envelopes, size: #9.

All designs should incorporate our brand colors, brand typeface, and logo. Please view attached brand guidelines document for brand colors, and brand description.

Letterhead: 8.5” x 11” Must include CoralvexKTN Logo, Dorrit Falke Certified Dealer Logo, mailing address, phone number, website, and email address.

Envelope: 9.5” x 4.125” Must include CoralvexKTN Logo, mailing address, and Dorrit Falke Certified Dealer Logo.

Attached files include:

```html
<!DOCTYPE html>
<html lang="en">
<head>
<meta charset="utf-8">
<title>CoralvexKTN Stationery</title>
<link href="https://fonts.googleapis.com/css2?family=Open+Sans:wght@400;600&family=Great+Vibes&display=swap" rel="stylesheet">
<style>
  :root {
    --backdrop: #3a3a3a;
    --paper: #ffffff;
    --sage: #5c7f70;
    --sage-line: #6f8f82;
    --ink: #4a4a4a;
    --ink-dark: #1f1f1f;
    --dealer: #e8401c;
    --faint: #e6e9e7;
    --faint-text: #eceeed;
  }
  * { box-sizing: border-box; margin: 0; padding: 0; }
  html, body { width: 1200px; height: 860px; overflow: hidden; }
  body {
    background: var(--backdrop);
    font-family: "Open Sans", Arial, sans-serif;
    color: var(--ink);
    position: relative;
  }
  .sheet { position: absolute; background: var(--paper); overflow: hidden; box-shadow: 0 6px 14px rgba(0,0,0,.45); }

  /* brand lockup */
  .brand { position: absolute; display: flex; align-items: center; }
  .brand-dot { border-radius: 50%; background: var(--sage); flex: none; }
  .brand-name { color: var(--sage); font-weight: 400; letter-spacing: .2px; line-height: 1; }
  .dealer { position: absolute; display: flex; align-items: center; }
  .dealer-badge { border-radius: 50%; background: var(--dealer); flex: none; }
  .dealer-name { color: var(--dealer); font-weight: 400; line-height: 1; letter-spacing: -.1px; }
  .rule { position: absolute; height: 1px; background: var(--sage-line); right: 0; }
  .faint-block { position: absolute; background: var(--faint); }

  /* envelope front */
  .envelope-front { left: 118px; top: 171px; width: 456px; height: 229px; }
  .envelope-front .brand { left: 15px; top: 15px; gap: 6px; }
  .envelope-front .brand-dot { width: 21px; height: 21px; }
  .envelope-front .brand-name { font-size: 16px; }
  .envelope-front .dealer { left: 15px; top: 41px; gap: 6px; }
  .envelope-front .dealer-badge { width: 15px; height: 15px; }
  .envelope-front .dealer-name { font-size: 7px; }
  .envelope-front .return-address { position: absolute; left: 15px; top: 59px; font-size: 4.6px; color: var(--ink); }
  .envelope-front .rule { left: 131px; top: 63px; }
  .envelope-front .faint-block { left: 325px; top: 140px; width: 131px; height: 89px; }

  /* envelope back */
  .envelope-back { left: 118px; top: 461px; width: 456px; height: 230px; }
  .flap { position: absolute; left: 0; top: 0; width: 100%; height: 63px; background: var(--sage); border-radius: 0 0 24px 24px; }
  .flap-mark { position: absolute; left: 208px; top: 11px; width: 40px; height: 40px; border-radius: 50%; background: rgba(255,255,255,.06); }
  .back-name { position: absolute; left: 0; right: 0; top: 71px; text-align: center; font-size: 26px; color: var(--faint-text); font-weight: 400; }

  /* letterhead */
  .letterhead { left: 637px; top: 118px; width: 446px; height: 624px; }
  .letterhead .brand { left: 14px; top: 29px; gap: 8px; }
  .letterhead .brand-dot { width: 25px; height: 25px; }
  .letterhead .brand-name { font-size: 21px; }
  .letterhead .dealer { left: 14px; top: 59px; gap: 6px; }
  .letterhead .dealer-badge { width: 19px; height: 19px; }
  .letterhead .dealer-name { font-size: 8.5px; }
  .letterhead .rule { left: 151px; top: 72px; }
  .letterhead .faint-block { left: 149px; top: 423px; width: 297px; height: 201px; }

  .recipient { position: absolute; left: 43px; top: 127px; line-height: 1.25; }
  .recipient-name { font-size: 7.5px; font-weight: 600; color: var(--sage); }
  .recipient-role { font-size: 6px; color: var(--ink-dark); }
  .letter-date { position: absolute; right: 42px; top: 147px; font-size: 7px; }

  .letter-body { position: absolute; left: 43px; top: 187px; width: 362px; }
  .letter-body p { font-size: 6.8px; line-height: 15.5px; margin-bottom: 15.5px; }

  .signoff { position: absolute; left: 337px; top: 450px; line-height: 1.15; }
  .signature { font-family: "Great Vibes", cursive; font-size: 17px; color: var(--ink-dark); }
  .signoff-name { font-size: 6.5px; font-weight: 600; color: var(--ink-dark); }
  .signoff-role { font-size: 6.5px; color: var(--ink-dark); }

  .address-band { position: absolute; left: 0; top: 585px; width: 148px; height: 30px; background: var(--sage); color: #fff; font-size: 7px; line-height: 11.5px; padding: 4px 0 0 14px; }
  .contact-list { position: absolute; left: 362px; top: 580px; border-left: 1px solid var(--ink); padding-left: 3px; list-style: none; }
  .contact-list li { display: flex; align-items: center; gap: 3px; font-size: 5.8px; line-height: 10.3px; color: var(--ink); }
  .contact-list svg { width: 5px; height: 5px; flex: none; }
</style>
</head>
<body>

  <section class="sheet envelope-front" aria-label="Envelope front">
    <div class="brand"><span class="brand-dot"></span><span class="brand-name">CoralvexKTN</span></div>
    <div class="dealer"><span class="dealer-badge"></span><span class="dealer-name">Dorrit Falke Certified Dealer</span></div>
    <p class="return-address">410 SW Larchmont, Suite 118 Eastbrook, OR 97015</p>
    <div class="rule"></div>
    <div class="faint-block"></div>
  </section>

  <section class="sheet envelope-back" aria-label="Envelope back">
    <div class="flap"><span class="flap-mark"></span></div>
    <p class="back-name">CoralvexKTN</p>
  </section>

  <section class="sheet letterhead" aria-label="Letterhead">
    <div class="brand"><span class="brand-dot"></span><span class="brand-name">CoralvexKTN</span></div>
    <div class="dealer"><span class="dealer-badge"></span><span class="dealer-name">Dorrit Falke Certified Dealer</span></div>
    <div class="rule"></div>
    <div class="faint-block"></div>

    <div class="recipient">
      <p class="recipient-name">John Doe</p>
      <p class="recipient-role">Chief Director</p>
    </div>
    <p class="letter-date">Date, 00 September, 2021</p>

    <div class="letter-body">
      <p>This is a sample letter that has been placed to demonstrate typing remat (Your Company). letterhead design. When positioned properly, it will serve to work in harmony with all other elements letterhead. This letterhead design is meant to project an image</p>
      <p>This letterhead design is meant project an image of professionalism reliability. By using simple aligen we have created a very spacious feeling. The simplicity suggest rengththe the spaciousnes contributes h aesthetics the layout. These basic qualities along with the (Your Company)</p>
      <p>look and helps reinforce the (Your Company) brand. letterhead design is meant to project an image p design. When positioned properly, it will serve to work in harmony all the other elements letterhead. sionalism and reliability.</p>
      <p>This letterhead design is based on the (Form of your logo) form (Your Company) logo. Each stationery we have created a very spacious feeling. The simplicity suggests strength the spaciousnes contribute part of the (Form of your logo).</p>
    </div>

    <div class="signoff">
      <p class="signature">John Doe</p>
      <p class="signoff-name">John Doe</p>
      <p class="signoff-role">Manager</p>
    </div>

    <div class="address-band">410 SW Larchmont, Suite 118<br>Eastbrook, OR 97015</div>

    <ul class="contact-list">
      <li><svg viewBox="0 0 10 10"><circle cx="5" cy="5" r="5" fill="#5c7f70"/></svg>555.014.2736</li>
      <li><svg viewBox="0 0 10 10"><circle cx="5" cy="5" r="5" fill="#5c7f70"/></svg>info@coralvexktn.com</li>
      <li><svg viewBox="0 0 10 10"><circle cx="5" cy="5" r="5" fill="#5c7f70"/></svg>www.coralvexktn.com</li>
    </ul>
  </section>

</body>
</html>
```